Tor'k Wayfarer Travel

We need a sleek, professional, inviting card to elicit global travel for the experienced and professional traveler. Royal blue, black and silver. (perhaps the wording could be silver with black shadow?-get creative) Maybe a watermark on the front and the full raised logo on the back.
We want a stylish and modern card, but professional.

```html
<!DOCTYPE html>
<html lang="en">
<head>
<meta charset="UTF-8">
<title>Tor'k Wayfarer Travel — Business Card</title>
<link rel="stylesheet" href="https://fonts.googleapis.com/css2?family=Roboto:wght@400;500&display=swap">
<style>
  :root {
    --backdrop: #3a3a3a;
    --card: #141414;
    --card-edge: #262626;
    --blue: #29a8e0;
    --green: #8dc63f;
  }
  * { margin: 0; padding: 0; box-sizing: border-box; }
  html, body { width: 1200px; height: 960px; overflow: hidden; }
  body {
    background: var(--backdrop);
    font-family: "Roboto", Arial, sans-serif;
    display: flex;
    flex-direction: column;
    align-items: center;
    justify-content: center;
    gap: 48px;
  }
  .card {
    position: relative;
    width: 700px;
    height: 400px;
    background: var(--card);
    border-radius: 24px;
    box-shadow: 0 0 0 1px var(--card-edge), 0 14px 30px rgba(0,0,0,.45);
    overflow: hidden;
  }
  .brand-name {
    display: flex;
    align-items: center;
    gap: 14px;
    color: var(--blue);
    font-weight: 500;
    text-transform: uppercase;
    letter-spacing: 1px;
    white-space: nowrap;
  }
  .brand-mark {
    width: 14px;
    height: 14px;
    background: var(--green);
    flex: none;
  }
  .card-front .brand-name {
    position: absolute;
    left: 50%;
    top: 50%;
    transform: translate(-50%, -50%);
    font-size: 40px;
  }
  .card-back .brand-name {
    position: absolute;
    right: 44px;
    top: 46px;
    font-size: 24px;
    gap: 10px;
  }
  .card-back .brand-mark { width: 10px; height: 10px; }
  .holder {
    position: absolute;
    left: 52px;
    top: 170px;
  }
  .holder-name { color: var(--blue); font-size: 22px; font-weight: 500; }
  .holder-title { color: var(--green); font-size: 16px; margin: 4px 0 0 14px; }
  .address {
    position: absolute;
    left: 66px;
    top: 250px;
    font-size: 17px;
    line-height: 21px;
    color: var(--green);
  }
  .address-label { color: var(--blue); }
  .contacts {
    position: absolute;
    left: 66px;
    top: 324px;
    list-style: none;
    font-size: 17px;
    line-height: 22px;
    color: var(--green);
  }
  .contacts li { display: flex; align-items: center; gap: 12px; }
  .contacts svg { width: 13px; height: 13px; fill: var(--blue); flex: none; }
</style>
</head>
<body>

<section class="card card-front" aria-label="Card front">
  <div class="brand-name"><span class="brand-mark"></span>Tor'k Wayfarer Travel</div>
</section>

<section class="card card-back" aria-label="Card back">
  <div class="brand-name"><span class="brand-mark"></span>Tor'k Wayfarer Travel</div>

  <div class="holder">
    <p class="holder-name">Delano Whitcombe</p>
    <p class="holder-title">Founder &amp; CEO</p>
  </div>

  <div class="address">
    <p class="address-label">Address:</p>
    <p>48 Harbor Crest Lane</p>
    <p>Suite 3B, Marlow, NC 28730</p>
  </div>

  <ul class="contacts">
    <li>
      <svg viewBox="0 0 16 16" aria-hidden="true"><path d="M3.6 1.2l2.2 2.9-1.3 1.7c.9 2 2.6 3.7 4.6 4.6l1.7-1.3 2.9 2.2-1.3 2.6C7.2 13.9 2.1 8.8 1 3.4z"/></svg>
      555-214-7390
    </li>
    <li>
      <svg viewBox="0 0 16 16" aria-hidden="true"><path d="M1 3h14v1.2L8 9 1 4.2z"/><path d="M1 6l7 4.8L15 6v7H1z"/></svg>
      info@yourmail.com
    </li>
    <li>
      <svg viewBox="0 0 16 16" aria-hidden="true"><circle cx="8" cy="8" r="7"/><path d="M1 8h14M8 1c-3 3.5-3 10.5 0 14M8 1c3 3.5 3 10.5 0 14" stroke="#141414" stroke-width="1" fill="none"/></svg>
      www.yourwebsite.com
    </li>
  </ul>
</section>

</body>
</html>
```